RESTAURANT MENU

WANTING TO CHANGE MENU DESIGN AND ADD SOME PLATES AND DESSERTS

ILL POST PICTURES OF LOGO AND PLATES. DONT HAVE ANYTHING IN MIND JUST NEED SOMETHING NEW THAT WILL STAND OUT .

Industry/Entity Type

Restaurant

Requirements
Must have
• THE SIZE RIGHT NOW IS 11X17 TRIFOLD MENU.
• IF ITS TOO CROWDED WITH THE NEW PLATES I DONT MIND MAKING IT BIGGER .
• ADD ONS
• ******************************** PASTAS **************************
• CHICKEN FETTUCCINE OR PENNE PASTA - 9.25
• SHRIMP FETTUCCINE OR PENNE PAST 10.25
• ******************* WINGS ***************************************
• BONELESS OR TRADITIONAL
• 5 WINGS - 5.99
• 10 WINGS - 8.99
• 20 WINGS - 14.99
• 50 WINGS - 35.99
• mild , hot , lemon pepper , sweet chili , teriyaki , garlic Parmesan
• *****************FROM THE BAR-B-QUE*************
• BABY BACK RIBS
• half rack - 12.99
• full rack - 18.99
• BRISKET BURGER 8.25
• BARBECUE COMBO - 17.99
• half rack of ribs, brisket , and sausage
• served with potato salad and red beans.
Should not have
• ADRESS CORRECTION ****
• 418 N. MARLOWE AVE.
• CEDAR FLATS
• ************* APPETIZERS***********
• Jalapeno cheese fries ............................. 4.99
• Mozzarella cheese sticks ........................ 5.25
• Classic Nachos ( ground bee) ................. 6.99
• Nachos ( fajita or chicken fajita ).............. 7.99
• Panchos ....................................................8.99
• ( includes lettuce , and avocado )
• Shrimp Nachos ........................................8.99
• Choriqueso...............................................6.99
• Guacamole ..............................................5.99
• ***************SALADS******************
• House Salad ...........................................5.99
• Caesar Salad...........................................5.99
• Chef Salad ...............................................7.99
• Grilled or Crispy chicken Salad ................8.99
• Shrimp Salad ............................................9.99
• ***************BURGERS AND SANDWICHES ****************
• Fajita Steak Burger .............................................................8.95
• (fine cut fajita loaded with fresh sauteed mushrooms , and topped with
• mozzarella cheese, crisp lettuce , onions , tomatoes mayo & mustard)
• Mushroom Swiss Burger .....................................................8.95
• (loaded with fresh saureed mushrooms, and topped with melted Swiss cheese)
• Hawaiian Burger ..................................................................7.99
• (topped with pineapple , american cheese , crisp lettuce , tomatoes and mayo. )
• Barbecue Burger.......................................................................7.99
• (basted with our original Bbq sauce, American cheese , lettuce , fresh tomatoes , mayo and mustard.)
• Patty Melt ................................................................................7.99
• Cheese Burger ........................................................................6.99
• Double Cheese Burger............................................................7.99
• Grilled or Fried Chicken Burger ................................................6.99
• Fish Burger ..............................................................................6.99
• (breaded fish with lettuce, tomatoes & tartar sauce )
• Blt..................................................................................4.99
• (bacon , lettuce & tomato sandwich )
• *******all burgers are served with french fries ***************
• *******ADD THREE SLICES OF BACON TO ANY BURGER ******
• ..................................1.25.
• **************KIDS MENU *****************
• Hamburger combo ..................................3.50
• cheese burger combo ..............................3.99
• Grilled ham and cheese ...........................3.50
• Chicken Tenders .......................................3.99
• Enchilada plate .........................................3.99
• (two enchiladas , rice & beans )
• Ground Beef tacos ...................................3.99
• (2 crispy or soft ground beef tacos , lettuce and cheese )
• ***************SPECIALTIES ***********************
• Chile Relleno ......................................................9.99
• (ground beef or cheese )
• Shrimp and cheese Chile Relleno ......................10.99
• Hamburger steak .................................................8.99
• 8 oz Grilled Chicken Breast .................................8.99
• Chicken Fried Chicken ........................................8.99
• Chicken Fried Steak .............................................8.99
• T Bone .................................................................12.99
• Pork Chops ..........................................................8.99
• Arrachera Steak ...................................................9.99
• ****************COMBINATION PLATES***********************
• Kandry's Special ..................................................8.99
• (fajita with two enchiladas on the side , rice and beans )
• Tampiquena .........................................................9.99
• (fajita steak with two enchiladas on the side , rice and beans
• Rio Bravo Plate .....................................................11.99
• (1 beef or cheese chile relleno with fajita steak on the side , rice and beans )
• Fajita & Shrimp plate .............................................11.99
• T Bone & Shrimp ......................................................13.99
• ************SOUTH OF THE BORDER ****************
• Cheese Enchiladaas ..................................................7.99
• Beef or Chicken Enchiladas ......................................8.99
• Mexican Plate .............................................................9.50
• (three enchiladas , one ground beef taco, and one chicken chalupa )
• Bean and Cheese Chalupa...........................................7.99
• Beef or Chicken Chalupas............................................8.99
• Chicken Flautas ..........................................................8.99
• Beef Milanesa .............................................................8.99
• Chicken Milanesa..........................................................8.99
• Bisteck Ranchero ..........................................................8.99
• Fajita or Chicken plate ...................................................8.99
• Fajita Toreada ................................................................8.99
• Pechuga Santa Fe.........................................................8.99
• Carne Guisada Plate......................................................8.99
• Fajita or Chicken Quesadillas .......................................9.99
• Shrimp Quesadillas ......................................................10.99
• Fajita or Chicken Tacos .................................................8.99
• Ground Beef tacos ( crispy or soft )...............................7.99
• **all Plates are served with rice and beans ***
• ****************TACOS ************
• Chicken fajita taco .....................................2.99
• Fajita taco ..................................................2.99
• Carne guisada ..........................................2.99
• Ground Beef taco ......................................2.50
• ************SOUPS ******************
• Caldo de Res ..........................small 6.99.................large....7.99
• Caldo de Pescado y Camaron ..small 7.99..............large ....8.99
• Caldo Siete Mares .....................small 8.99.............large ....9.99
• Menudo ....................................small ..6.99.............large ..7.99
• Caldo Tlalpeno ..........................small .. 7.99........large 8.99
• *********SEAFOOD*************
• Fish Tacos .................................................8.99
• (fish filet on corn tortilla , rice on the side )
• Fish Plate (Grilled or Fried ).........................11.99
• Shrimp Plate (any style)................................12.99
• (al mojo de ajo, ala diabla, agua chiles , fried)
• Costa Azul ....................................................14.99
• ( 6 shrimp wrapped in bacon and breaded to perfection , filled with mozzarella cheese , served with fries , rice and salad )
• Seafood Fiesta .............................................14.99
• ( combination of fish , shrimp and crab)
• Shrimp Cocktail .......................................small ..9.99.....large...12.99
• ***********FAMILY PLATTERS **************************
• Botana or Sombrero for 1 .............................................10.99
• Botana or Sombrero for 2 ..............................................20.99
• Botana or Sombrero for 3 ..............................................27.99
• Botana or Sombrero for 4 ..............................................38.99
• Botana or Sombrero for 6................................................49.99
• (beef chicken or mixed )
• Seafood platter for 2 ........................................................25.99
• Seafood platter for 3 ........................................................33.99
• Seafood platter for 4 ........................................................44.99
• Seafood platter for 6.........................................................59.99
• Mar y Tierra for 2 ............................................................26.99
• Mar y Tierra for 3 ............................................................35.99
• Mar y Tierra for 4 .............................................................43.99
• Mar y Tierra for 6...............................................................58.99
• *********BREAKFAST PLATES *************************
• Potato & Egg Plate ...................................4.99
• Bacon & Egg Plate ....................................4.99
• Migas & Egg Plate.....................................4.99
• Huevos Rancheros ...................................4.99
• Huevo ala Mexicana ..................................4.99
• Chorizo & Egg Plate ..................................4.99
• Sausage & Egg Plate ................................4.99
• Ham & Egg Plate........................................4.99
• Machacado & Egg Plate ............................5.99
• Chicharron en Salsa.....................................5.99
• Chicharron & Egg Plate................................5.99
• Chicharron en salsa with 2 eggs ..................6.99
• Chilaquiles .................................................5.99
• Huevos Divorciados ...................................6.99
• Chicken Chilaquiles ..................................6.99
• Fajita Asada & egg ......................................7.99
• Barbacoa Plate ............................................6.99
• ( add two eggs )............................................7.99
• **************GOURMET BREAKFAST*****
• Kandry's Favorite .............................................7.99
• two eggs , one slice of ham , two bacon , two sausage links and two buttermilk pancakes
• Kandry's Special ..........................................................3.99
• Two eggs , sausage , ham or bacon
• Ham and cheese Omelette .......................................6.99
• three egg omelette filled with ham and cheese , hash-brown and toast.
• Ultimate Omelette ....................................................7.99
• Three egg omelette with sausage , bacon , fire roasted bell peppers and onion , mushrooms , diced tomatoes and shredded cheese . served with hash-browns and toast .
• Meat lovers Omelette ......................................................8.99
• Three egg omelette with grilled steak , fire roasted bell peppers and onions.
• sauteed mushrooms and melted mozzarella cheese.
• The steakwich ...............................................7.99
• two scrambled eggs, tender steak , american cheese on texas toast .
• Hamwich .......................................................5.99
• sausagewich .................................................5.99
• Chicken Fried steak and eggs .......................7.99
• Pork chops and Eggs .....................................9.99
• T Bone Steak and eggs ...............................10.99
• **********BREAKFAST TACOS ********************
• Bacon & egg ...................1.99
• Sausage & Egg ................1.99
• Potato & Egg...................1.99
• Chorizo & Egg .................1.99
• Bean &Egg.......................1.99
• Ham and Egg ....................1.99
• Machacado & Egg ............2.59
• Chicharron & Egg .............2.59
• Gorditas .............................2.99
• *****extra taco filling *** .35
• *********DRINKS ***********
• Coffee..............................1.99
• Milk ..................................1.99
• Orange Juice ...................2.50
• (no refill )
• Sweet & unsweet Tea ..........2.15
• Raspberry Tea ...................2.50
• Fountain Drinks ..................2.15
• Strawberry lemonade ...........2.50
• Lemonade .............................2.50
• hot chocolate ...........................1.99
• *****15% WILL BE ADDED ON TABLES OF 6 OR MORE ***

```html
<!DOCTYPE html>
<html lang="en">
<head>
<meta charset="utf-8">
<title>Kandry's Menu</title>
<link rel="stylesheet" href="https://fonts.googleapis.com/css2?family=Arimo:wght@400;700&family=Arvo:wght@400;700&display=swap">
<style>
:root{
  --backdrop:#f7f19a;
  --sheet:#bfd38e;
  --sheet-light:#d3e2a6;
  --frame:#2f3029;
  --ink:#2d2a1e;
  --badge:#d8c8a0;
  --badge-edge:#6b5534;
  --wood:#b97436;
  --wood-light:#c98a48;
  --wood-seam:#8a4f1f;
  --parchment:#efe0b8;
  --cover-ink:#3a2412;
  --trim:#8a9a5c;
}
*{margin:0;padding:0;box-sizing:border-box}
html,body{width:1200px;height:1200px;overflow:hidden;background:var(--backdrop)}
body{position:relative;font-family:"Arimo",Arial,sans-serif;color:var(--ink)}
.sheet{position:absolute;left:152px;width:902px;box-shadow:0 3px 10px rgba(0,0,0,.25)}
.sheet-outer{top:6px;height:584px;display:flex}
.sheet-inner{top:604px;height:584px;background:radial-gradient(ellipse at 50% 40%,var(--sheet-light),var(--sheet))}
.inside{position:relative;width:590px;height:100%;background:radial-gradient(ellipse at 50% 40%,var(--sheet-light),var(--sheet))}
.inside::before{content:"";position:absolute;left:8px;top:8px;right:0;bottom:14px;border:5px solid var(--frame);border-right:none}
.cover{position:relative;flex:1;background:repeating-linear-gradient(180deg,var(--wood-light) 0 26px,var(--wood) 26px 52px,var(--wood-seam) 52px 54px)}
.col{position:absolute;top:30px;font-size:7.4px;line-height:10.6px}
.badge{display:table;margin:0 auto 8px;padding:2px 14px;background:var(--badge);border:1px solid var(--badge-edge);border-left-width:4px;border-right-width:4px;font-family:"Arvo",Georgia,serif;font-size:8.4px;letter-spacing:.3px;text-transform:uppercase;color:#3b2d1a}
.section{margin-bottom:6px}
.row{display:flex;align-items:baseline;white-space:nowrap}
.row .dots{flex:1;border-bottom:1px dotted #555;margin:0 1px;transform:translateY(-2px)}
.note{white-space:nowrap}
.caps{text-transform:uppercase}
.center{text-align:center}
.pair{display:flex;gap:12px}
.pair>div{flex:1}
.banner{margin-top:8px;padding:2px 8px;background:var(--badge);border:1px solid var(--badge-edge);border-left-width:4px;border-right-width:4px;font-family:"Arvo",Georgia,serif;font-size:8px;text-align:center}
.sheet-inner .border-dash{position:absolute;inset:10px 12px;border:1px dashed var(--trim)}
.sheet-inner .divider{position:absolute;top:14px;bottom:14px;border-left:1px dashed var(--trim)}
.art{position:absolute}
.scroll-top{left:18px;top:26px;width:276px;height:240px;background:linear-gradient(180deg,#f2e6c4,#dcc79a);border-radius:6px}
.brand{position:absolute;left:18px;top:200px;width:276px;text-align:center;font-family:"Arvo",Georgia,serif;font-weight:700;font-size:40px;color:#d9a021}
.menu-word{left:84px;top:290px;width:150px;height:86px;background:radial-gradient(ellipse,#f2d84a,#b69224);border-radius:40px}
.cactus{left:226px;top:360px;width:34px;height:52px;background:linear-gradient(#5aa04a,#3c7a30);border-radius:14px}
.contact{position:absolute;left:22px;top:410px;width:270px;height:132px;background:linear-gradient(180deg,var(--parchment),#dfcb9c);border:1px solid #b89a63;text-align:center;font-family:"Arvo",Georgia,serif;color:var(--cover-ink);font-weight:700}
.contact .addr{margin-top:30px;font-size:11px}
.contact .phone{margin-top:16px;font-size:19px}
.contact .web{margin-top:14px;font-size:10px}
.photo{position:absolute;border-radius:50%}
</style>
</head>
<body>

<section class="sheet sheet-outer">
  <div class="inside">
    <div class="col" style="left:37px;width:232px">
      <div class="section">
        <div class="badge">Seafood</div>
        <div class="row"><span>Fish Tacos(fish filet on corn tortilla, rice on the side )</span><span class="dots"></span><span>8.99</span></div>
        <div class="row"><span>Fish Plate (Grilled or Fried )</span><span class="dots"></span><span>11.99</span></div>
        <div class="row"><span>Shrimp Plate (any style)</span><span class="dots"></span><span>12.99</span></div>
        <div class="note">(al mojo de ajo, ala diabla, agua chiles, fried)</div>
        <div class="row"><span>Costa Azul</span><span class="dots"></span><span>14.99</span></div>
        <div class="note">( 6 shrimp wrapped in bacon and breaded to perfection , filled with</div>
        <div class="note">mozzarella cheese, served with fries, rice and salad )</div>
        <div class="row"><span>Seafood Fiesta ( combination of fish, shrimp and crab)</span><span class="dots"></span><span>14.99</span></div>
        <div class="row"><span>Shrimp Cocktail</span><span class="dots"></span><span>small ......9.99.....large......12.99</span></div>
      </div>
      <div class="section" style="width:146px">
        <div class="badge">Family Platters</div>
        <div class="row"><span>Botana or Sombrero for 1</span><span class="dots"></span><span>10.99</span></div>
        <div class="row"><span>Botana or Sombrero for 2</span><span class="dots"></span><span>20.99</span></div>
        <div class="row"><span>Botana or Sombrero for 3</span><span class="dots"></span><span>27.99</span></div>
        <div class="row"><span>Botana or Sombrero for 4</span><span class="dots"></span><span>38.99</span></div>
        <div class="row"><span>Botana or Sombrero for 6</span><span class="dots"></span><span>49.99</span></div>
        <div class="note">( beef chicken or mixed )</div>
        <div class="row"><span>Seafood platter for 2</span><span class="dots"></span><span>25.99</span></div>
        <div class="row"><span>Seafood platter for 3</span><span class="dots"></span><span>33.99</span></div>
        <div class="row"><span>Seafood platter for 4</span><span class="dots"></span><span>44.99</span></div>
        <div class="row"><span>Seafood platter for 6</span><span class="dots"></span><span>59.99</span></div>
        <div class="row"><span>Mar y Tierra for 2</span><span class="dots"></span><span>26.99</span></div>
        <div class="row"><span>Mar y Tierra for 3</span><span class="dots"></span><span>35.99</span></div>
        <div class="row"><span>Mar y Tierra for 4</span><span class="dots"></span><span>43.99</span></div>
        <div class="row"><span>Mar y Tierra for 6</span><span class="dots"></span><span>58.99</span></div>
      </div>
      <div class="section" style="width:138px">
        <div class="badge">Breakfast Plates</div>
        <div class="row"><span>Potato &amp; Egg Plate</span><span class="dots"></span><span>4.99</span></div>
        <div class="row"><span>Bacon &amp; Egg Plate</span><span class="dots"></span><span>4.99</span></div>
        <div class="row"><span>Migas &amp; Egg Plate</span><span class="dots"></span><span>4.99</span></div>
        <div class="row"><span>Huevos Rancheros</span><span class="dots"></span><span>4.99</span></div>
        <div class="row"><span>Huevo ala Mexicana</span><span class="dots"></span><span>4.99</span></div>
        <div class="row"><span>Chorizo &amp; Egg Plate</span><span class="dots"></span><span>4.99</span></div>
        <div class="row"><span>Sausage &amp; Egg Plate</span><span class="dots"></span><span>4.99</span></div>
        <div class="row"><span>Ham &amp; Egg Plate</span><span class="dots"></span><span>4.99</span></div>
        <div class="row"><span>Machacado &amp; Egg Plate</span><span class="dots"></span><span>5.99</span></div>
        <div class="row"><span>Chicharron en Salsa</span><span class="dots"></span><span>5.99</span></div>
        <div class="row"><span>Chicharron &amp; Egg Plate</span><span class="dots"></span><span>5.99</span></div>
        <div class="row"><span>Chicharron en salsa with 2 eggs</span><span class="dots"></span><span>6.99</span></div>
        <div class="row"><span>Chilaquiles</span><span class="dots"></span><span>5.99</span></div>
        <div class="row"><span>Huevos Divorciados</span><span class="dots"></span><span>6.99</span></div>
        <div class="row"><span>Chicken Chilaquiles</span><span class="dots"></span><span>6.99</span></div>
        <div class="row"><span>Fajita Asada &amp; egg</span><span class="dots"></span><span>7.99</span></div>
        <div class="row"><span>Barbacoa Plate</span><span class="dots"></span><span>6.99</span></div>
        <div class="row"><span>( add two eggs )</span><span class="dots"></span><span>7.99</span></div>
      </div>
    </div>

    <div class="col" style="left:322px;width:262px">
      <div class="section">
        <div class="badge">Gourmet Breakfast</div>
        <div class="row"><span>Kandry's Favorite</span><span class="dots"></span><span>7.99</span></div>
        <div class="note">two eggs, one slice of ham, two bacon,</div>
        <div class="note">two sausage links and two buttermilk pancakes</div>
        <div class="row"><span>Kandry's Special</span><span class="dots"></span><span>3.99</span></div>
        <div class="note">Two eggs , sausage , ham or bacon</div>
        <div class="row"><span>Ham and cheese Omelette</span><span class="dots"></span><span>6.99</span></div>
        <div class="note">three egg omelette filled with ham and cheese, hash-brown and toast.</div>
        <div class="row"><span>Ultimate Omelette</span><span class="dots"></span><span>7.99</span></div>
        <div class="note">Three egg omelette with sausage, bacon, fire roasted</div>
        <div class="note">bell peppers and onion, mushrooms, diced tomatoes</div>
        <div class="note">and shredded cheese served with hash-browns and toast .</div>
        <div class="row"><span>Meat lovers Omelette</span><span class="dots"></span><span>8.99</span></div>
        <div class="note">Three egg omelette with grilled steak, fire roasted bell peppers and</div>
        <div class="note">onions sauteed mushrooms and melted mozzarella cheese.</div>
        <div class="row"><span>The steakwich</span><span class="dots"></span><span>7.99</span></div>
        <div class="note">two scrambled eggs, tender steak , american cheese on texas toast .</div>
        <div class="row"><span>Hamwich</span><span class="dots"></span><span>5.99</span></div>
        <div class="row"><span>Sausagewich</span><span class="dots"></span><span>5.99</span></div>
        <div class="row"><span>Chicken Fried steak and eggs</span><span class="dots"></span><span>7.99</span></div>
        <div class="row"><span>Pork chops and Eggs</span><span class="dots"></span><span>9.99</span></div>
        <div class="row"><span>T Bone Steak and eggs</span><span class="dots"></span><span>10.99</span></div>
      </div>
      <div class="section">
        <div class="badge">Breakfast Tacos</div>
        <div style="width:104px">
          <div class="row"><span>Bacon &amp; egg</span><span class="dots"></span><span>1.99</span></div>
          <div class="row"><span>Sausage &amp; Egg</span><span class="dots"></span><span>1.99</span></div>
          <div class="row"><span>Potato &amp; Egg</span><span class="dots"></span><span>1.99</span></div>
          <div class="row"><span>Chorizo &amp; Egg</span><span class="dots"></span><span>1.99</span></div>
          <div class="row"><span>Bean &amp;Egg</span><span class="dots"></span><span>1.99</span></div>
          <div class="row"><span>Ham and Egg</span><span class="dots"></span><span>1.99</span></div>
          <div class="row"><span>Machacado &amp; Egg</span><span class="dots"></span><span>2.59</span></div>
          <div class="row"><span>Chicharron &amp; Egg</span><span class="dots"></span><span>2.59</span></div>
          <div class="row"><span>Gorditas</span><span class="dots"></span><span>2.99</span></div>
          <div class="row"><span>extra taco filling</span><span class="dots"></span><span>0.35</span></div>
        </div>
      </div>
      <div class="section">
        <div class="badge">Drinks</div>
        <div class="pair" style="width:210px">
          <div class="row"><span>Coffee</span><span class="dots"></span><span>1.99</span></div>
          <div class="row"><span>Milk</span><span class="dots"></span><span>1.99</span></div>
          <div class="row"><span>Orange Juice</span><span class="dots"></span><span>2.50</span></div>
        </div>
        <div class="center" style="margin:10px 0">NO REFILL</div>
        <div class="pair" style="width:220px">
          <div>
            <div class="row"><span>Sweet &amp; unsweet Tea</span><span class="dots"></span><span>2.15</span></div>
            <div class="row"><span>Fountain Drinks</span><span class="dots"></span><span>2.15</span></div>
            <div class="row"><span>Lemonade</span><span class="dots"></span><span>2.50</span></div>
          </div>
          <div>
            <div class="row"><span>Raspberry Tea</span><span class="dots"></span><span>2.50</span></div>
            <div class="row"><span>Strawberry lemonade</span><span class="dots"></span><span>2.50</span></div>
            <div class="row"><span>Hot chocolate</span><span class="dots"></span><span>1.99</span></div>
          </div>
        </div>
        <div class="banner">15% WILL BE ADDED ON TABLES OF 6 OR MORE</div>
      </div>
    </div>
  </div>

  <div class="cover">
    <div class="art scroll-top" role="img" aria-label="Parchment scroll with sombrero-wearing sun mascot"></div>
    <div class="brand">Kandry's</div>
    <div class="art menu-word" role="img" aria-label="Decorative MENU title lettering with swirls"></div>
    <div class="art cactus" role="img" aria-label="Small cactus wearing a sombrero"></div>
    <div class="contact">
      <div class="addr">418 N. MARLOWE AVE. CEDAR FLATS</div>
      <div class="phone">Call us : 555-310-0148</div>
      <div class="web">www.kandrysrestaurant.com</div>
    </div>
  </div>
</section>

<section class="sheet sheet-inner">
  <div class="border-dash"></div>
  <div class="divider" style="left:308px"></div>
  <div class="divider" style="left:592px"></div>

  <div class="col" style="left:43px;width:230px">
    <div class="section caps" style="width:196px">
      <div class="badge">Pastas</div>
      <div class="row"><span>Chicken Fettuccine or Penne Pasta</span><span class="dots"></span><span>9.25</span></div>
      <div class="row"><span>Shrimp Fettuccine or Penne Past</span><span class="dots"></span><span>10.25</span></div>
    </div>
    <div class="section">
      <div class="badge">Wings</div>
      <div class="note caps">Boneless or Traditional</div>
      <div style="width:102px">
        <div class="row caps"><span>5 Wings</span><span class="dots"></span><span>5.99</span></div>
        <div class="row caps"><span>10 Wings</span><span class="dots"></span><span>8.99</span></div>
        <div class="row caps"><span>20 Wings</span><span class="dots"></span><span>14.99</span></div>
        <div class="row caps"><span>50 Wings</span><span class="dots"></span><span>35.99</span></div>
      </div>
      <div class="note">mild , hot , lemon pepper , sweet chili , teriyaki , garlic Parmesan</div>
    </div>
    <div class="section">
      <div class="badge">From the Bar-B-Que</div>
      <div class="note caps">Baby Back Ribs</div>
      <div style="width:106px">
        <div class="row"><span>half rack</span><span class="dots"></span><span>12.99</span></div>
        <div class="row"><span>full rack</span><span class="dots"></span><span>18.99</span></div>
        <div class="row caps"><span>Brisket Burger</span><span class="dots"></span><span>8.25</span></div>
        <div class="row caps"><span>Barbecue Combo</span><span class="dots"></span><span>17.99</span></div>
      </div>
      <div class="note">half rack of ribs, brisket , and sausage</div>
      <div class="note">served with potato salad and red beans.</div>
    </div>
    <div class="section" style="width:190px">
      <div class="badge">Appetizers</div>
      <div class="row"><span>Jalapeno cheese fries</span><span class="dots"></span><span>4.99</span></div>
      <div class="row"><span>Mozzarella cheese sticks</span><span class="dots"></span><span>5.25</span></div>
      <div class="row"><span>Classic Nachos ( ground bee)</span><span class="dots"></span><span>6.99</span></div>
      <div class="row"><span>Nachos ( fajita or chicken fajita )</span><span class="dots"></span><span>7.99</span></div>
      <div class="row"><span>Panchos</span><span class="dots"></span><span>8.99</span></div>
      <div class="note">( includes lettuce , and avocado )</div>
      <div class="row"><span>Shrimp Nachos</span><span class="dots"></span><span>8.99</span></div>
      <div class="row"><span>Choriqueso</span><span class="dots"></span><span>6.99</span></div>
      <div class="row"><span>Guacamole</span><span class="dots"></span><span>5.99</span></div>
    </div>
    <div class="section" style="width:190px">
      <div class="badge">Salads</div>
      <div class="row"><span>House Salad</span><span class="dots"></span><span>5.99</span></div>
      <div class="row"><span>Caesar Salad</span><span class="dots"></span><span>5.99</span></div>
      <div class="row"><span>Chef Salad</span><span class="dots"></span><span>7.99</span></div>
      <div class="row"><span>Grilled or Crispy chicken Salad</span><span class="dots"></span><span>8.99</span></div>
      <div class="row"><span>Shrimp Salad</span><span class="dots"></span><span>9.99</span></div>
    </div>
  </div>
  <div class="photo" role="img" aria-label="Plate of enchiladas with rice, broccoli and salsa" style="left:180px;top:192px;width:118px;height:76px;background:radial-gradient(ellipse,#f0dc9a,#e8e2cf 70%,#cfc7ad)"></div>
  <div class="photo" role="img" aria-label="Platter of shrimp salad" style="left:116px;top:494px;width:104px;height:56px;border-radius:4px;background:linear-gradient(135deg,#f4efe2,#d9cf9e 60%,#9eb46a)"></div>

  <div class="col" style="left:328px;width:212px">
    <div class="section">
      <div class="badge">Burgers and Sandwiches</div>
      <div class="row"><span>Fajita Steak Burger</span><span class="dots"></span><span>8.95</span></div>
      <div class="note">( fine cut fajita loaded with fresh sauteed</div>
      <div class="note">mushrooms, and topped with mozzarella cheese,</div>
      <div class="note">crisp lettuce, onions , tomatoes mayo &amp; mustard )</div>
      <div class="row"><span>Mushroom Swiss Burger</span><span class="dots"></span><span>8.95</span></div>
      <div class="note">( loaded with fresh saureed mushrooms, and</div>
      <div class="note">topped with melted Swiss cheese )</div>
      <div class="row"><span>Hawaiian Burger</span><span class="dots"></span><span>7.99</span></div>
      <div class="note">( topped with pineapple, american cheese,</div>
      <div class="note">crisp lettuce, tomatoes and mayo )</div>
      <div class="row"><span>Barbecue Burger</span><span class="dots"></span><span>7.99</span></div>
      <div class="note">( basted with our original Bbq sauce, American</div>
      <div class="note">cheese, lettuce, fresh tomatoes, mayo and mustard )</div>
      <div class="row"><span>Patty Melt</span><span class="dots"></span><span>7.99</span></div>
      <div class="row"><span>Cheese Burger</span><span class="dots"></span><span>6.99</span></div>
      <div class="row"><span>Double Cheese Burger</span><span class="dots"></span><span>7.99</span></div>
      <div class="row"><span>Grilled or Fried Chicken Burger</span><span class="dots"></span><span>6.99</span></div>
      <div class="row"><span>Fish Burger</span><span class="dots"></span><span>6.99</span></div>
      <div class="note">( breaded fish with lettuce, tomatoes &amp; tartar sauce )</div>
      <div class="row"><span>BLT</span><span class="dots"></span><span>4.99</span></div>
      <div class="note">( bacon , lettuce &amp; tomato sandwich )</div>
      <div class="note">all burgers are served with french fries</div>
      <div class="row"><span>add three slices of bacon to any burger</span><span class="dots"></span><span>1.25</span></div>
    </div>
    <div class="section">
      <div class="badge">Kids Menu</div>
      <div style="width:132px">
        <div class="row"><span>Hamburger combo</span><span class="dots"></span><span>3.50</span></div>
        <div class="row"><span>Cheese burger combo</span><span class="dots"></span><span>3.99</span></div>
        <div class="row"><span>Grilled ham and cheese</span><span class="dots"></span><span>3.50</span></div>
        <div class="row"><span>Chicken Tenders</span><span class="dots"></span><span>3.99</span></div>
        <div class="row"><span>Enchilada plate</span><span class="dots"></span><span>3.99</span></div>
        <div class="note">(two enchiladas , rice &amp; beans )</div>
        <div class="row"><span>Ground Beef tacos</span><span class="dots"></span><span>3.99</span></div>
      </div>
      <div class="note">(2 crispy or soft ground beef tacos , lettuce and cheese )</div>
    </div>
    <div class="section" style="width:198px">
      <div class="badge">Specialties</div>
      <div class="row"><span>Chile Relleno</span><span class="dots"></span><span>9.99</span></div>
      <div class="note">(ground beef or cheese )</div>
      <div class="row"><span>Shrimp and cheese Chile Relleno</span><span class="dots"></span><span>10.99</span></div>
      <div class="row"><span>Hamburger steak</span><span class="dots"></span><span>8.99</span></div>
      <div class="row"><span>8 oz Grilled Chicken Breast</span><span class="dots"></span><span>8.99</span></div>
      <div class="row"><span>Chicken Fried Chicken</span><span class="dots"></span><span>8.99</span></div>
      <div class="row"><span>Chicken Fried Steak</span><span class="dots"></span><span>8.99</span></div>
      <div class="row"><span>T Bone</span><span class="dots"></span><span>12.99</span></div>
      <div class="row"><span>Pork Chops</span><span class="dots"></span><span>8.99</span></div>
      <div class="row"><span>Arrachera Steak</span><span class="dots"></span><span>9.99</span></div>
    </div>
  </div>

  <div class="col" style="left:612px;width:230px">
    <div class="section" style="width:164px">
      <div class="badge">Combination Plates</div>
      <div class="row"><span>Kandry's Special</span><span class="dots"></span><span>8.99</span></div>
      <div class="note">( fajita with two enchiladas on the side, rice and beans )</div>
      <div class="row"><span>Tampiquena</span><span class="dots"></span><span>9.99</span></div>
      <div class="note">( fajita steak with two enchiladas on the side , rice and beans )</div>
      <div class="row"><span>Rio Bravo Plate</span><span class="dots"></span><span>11.99</span></div>
      <div class="note">( 1 beef or cheese chile relleno with fajita</div>
      <div class="note">steak on the side , rice and beans )</div>
      <div class="row"><span>Fajita &amp; Shrimp plate</span><span class="dots"></span><span>11.99</span></div>
      <div class="row"><span>T Bone &amp; Shrimp</span><span class="dots"></span><span>13.99</span></div>
    </div>
    <div class="section" style="width:164px">
      <div class="badge">South of the Border</div>
      <div class="row"><span>Cheese Enchiladaas</span><span class="dots"></span><span>7.99</span></div>
      <div class="row"><span>Beef or Chicken Enchiladas</span><span class="dots"></span><span>8.99</span></div>
      <div class="row"><span>Mexican Plate</span><span class="dots"></span><span>9.50</span></div>
      <div class="note">( three enchiladas , one ground beef taco,</div>
      <div class="note">and one chicken chalupa )</div>
      <div class="row"><span>Bean and Cheese Chalupa</span><span class="dots"></span><span>7.99</span></div>
      <div class="row"><span>Beef or Chicken Chalupas</span><span class="dots"></span><span>8.99</span></div>
      <div class="row"><span>Chicken Flautas</span><span class="dots"></span><span>8.99</span></div>
      <div class="row"><span>Beef Milanesa</span><span class="dots"></span><span>8.99</span></div>
      <div class="row"><span>Chicken Milanesa</span><span class="dots"></span><span>8.99</span></div>
      <div class="row"><span>Bisteck Ranchero</span><span class="dots"></span><span>8.99</span></div>
      <div class="row"><span>Fajita or Chicken plate</span><span class="dots"></span><span>8.99</span></div>
      <div class="row"><span>Fajita Toreada</span><span class="dots"></span><span>8.99</span></div>
      <div class="row"><span>Pechuga Santa Fe</span><span class="dots"></span><span>8.99</span></div>
      <div class="row"><span>Carne Guisada Plate</span><span class="dots"></span><span>8.99</span></div>
      <div class="row"><span>Fajita or Chicken Quesadillas</span><span class="dots"></span><span>9.99</span></div>
      <div class="row"><span>Shrimp Quesadillas</span><span class="dots"></span><span>10.99</span></div>
      <div class="row"><span>Fajita or Chicken Tacos</span><span class="dots"></span><span>8.99</span></div>
      <div class="row"><span>Ground Beef tacos ( crispy or soft )</span><span class="dots"></span><span>7.99</span></div>
      <div class="note">All Plates are served with rice and beans</div>
    </div>
    <div class="section" style="width:164px">
      <div class="badge">Tacos</div>
      <div style="width:104px">
        <div class="row"><span>Chicken fajita taco</span><span class="dots"></span><span>2.99</span></div>
        <div class="row"><span>Fajita taco</span><span class="dots"></span><span>2.99</span></div>
        <div class="row"><span>Carne guisada</span><span class="dots"></span><span>2.99</span></div>
        <div class="row"><span>Ground Beef taco</span><span class="dots"></span><span>2.50</span></div>
      </div>
    </div>
    <div class="section" style="width:224px">
      <div class="badge" style="margin-left:74px">Soups</div>
      <div class="row"><span>Caldo de Res</span><span class="dots"></span><span>small ..6.99 ........large ..7.99</span></div>
      <div class="row"><span>Caldo de Pescado y Camaron</span><span class="dots"></span><span>small ..7.99 ........large ..8.99</span></div>
      <div class="row"><span>Caldo Siete Mares</span><span class="dots"></span><span>small ..8.99 ........large ..9.99</span></div>
      <div class="row"><span>Menudo</span><span class="dots"></span><span>small ..6.99 ........large ..7.99</span></div>
      <div class="row"><span>Caldo Tlalpeno</span><span class="dots"></span><span>small ..7.99 ........large ..8.99</span></div>
    </div>
  </div>
  <div class="photo" role="img" aria-label="Plate of fajita tacos with lime and salsa" style="left:760px;top:400px;width:110px;height:80px;background:radial-gradient(ellipse,#8a6a3a,#c9b46a 60%,#e4dcb8)"></div>
</section>

</body>
</html>
```